New Website for Belcourt Manor at www.belcourt.com.au

A new logo has been designed (through pixel forge) and we now want to align the look and feel of our website at www.belcourt.com.au to the new logo. The content and page names (e.g. Grounds) will remain largely unchanged for the new site, so please submit a new look "Home" page, using our new logo, current text and any photos you choose from the existing gallery at our website. I have also attached the current "Home" page photos.

Industry/Entity Type

Accommodation

Number of Pages Required

1 page

Requirements
Must have
• Logo to be presented on white background.

```html
<!DOCTYPE html>
<html lang="en">
<head>
<meta charset="utf-8">
<title>Belcourt Manor – Home</title>
<link href="https://fonts.googleapis.com/css2?family=Raleway:wght@300;400;600;700&family=Open+Sans:wght@400;600&display=swap" rel="stylesheet">
<style>
:root{
  --brand:#1f6fb4;
  --brand-dark:#175a93;
  --ink:#3a3a3a;
  --muted:#7a7a7a;
  --line:#d9dde2;
  --footer:#2c2c2c;
  --white:#ffffff;
  --dusk-1:#3b4a63;
  --dusk-2:#8a6a52;
  --pool:#6fb3d6;
}
*{box-sizing:border-box;margin:0;padding:0}
html,body{width:878px;height:1200px;overflow:hidden;background:var(--white)}
body{font-family:"Open Sans",Arial,sans-serif;color:var(--ink);position:relative}
.site-header{height:64px;display:flex;align-items:center;justify-content:space-between;padding:0 30px 0 18px;background:var(--white)}
.brand{display:flex;align-items:center;gap:8px;font-family:"Raleway",sans-serif;font-weight:600;font-size:17px;color:var(--brand)}
.brand-dot{width:22px;height:22px;border-radius:50%;background:var(--pool)}
.main-nav{display:flex;align-items:center;font-family:"Raleway",sans-serif;font-size:10.5px;font-weight:600;color:var(--ink)}
.main-nav span{padding:0 4px}
.main-nav .sep{padding:0;color:var(--muted)}
.hero{position:relative;height:520px}
.hero-photo{position:absolute;inset:0;background:
  linear-gradient(180deg,rgba(255,255,255,0) 55%,rgba(255,255,255,.9) 78%,#fff 100%),
  linear-gradient(180deg,var(--dusk-1) 0%,#6a6e78 30%,var(--dusk-2) 50%,var(--pool) 68%,#c9d8e2 85%)}
.reservation{position:absolute;left:0;right:0;top:318px;text-align:center}
.section-title{font-family:"Raleway",sans-serif;font-weight:400;color:var(--ink)}
.reservation .section-title{font-size:24px}
.reservation .lead{font-size:9px;color:var(--muted);margin-top:6px}
.res-form{display:flex;justify-content:center;gap:16px;margin-top:24px}
.field{width:108px;text-align:left}
.field label{display:block;font-size:7px;color:var(--muted);margin-bottom:3px;text-transform:uppercase}
.field div{height:14px;border:1px solid var(--line);background:var(--white)}
.btn{display:inline-block;background:var(--brand);color:var(--white);font-family:"Raleway",sans-serif;font-weight:700;font-size:10px;letter-spacing:.5px;text-align:center}
.res-btn{margin-top:22px;width:118px;height:30px;line-height:30px;font-size:11px}
.welcome{text-align:center;margin-top:2px}
.welcome .section-title{font-size:27px}
.intro{display:flex;gap:30px;margin:18px 0 0 97px;width:680px}
.intro-photo{width:180px;height:140px;flex:none;background:linear-gradient(160deg,#7fa57a,#b4694b 45%,#5fb0d8 75%,#6d8b5a)}
.intro-text{flex:1;display:flex;gap:12px}
.intro-copy{flex:1}
.intro-copy h3{font-family:"Raleway",sans-serif;font-weight:700;font-size:12px;margin-bottom:6px}
.intro-copy p,.intro-copy li{font-size:7px;line-height:1.45;color:var(--muted);margin-bottom:4px}
.intro-copy ul{list-style:none;margin-top:4px}
.intro-copy li::before{content:"";display:inline-block;width:4px;height:4px;background:var(--brand);margin-right:5px;vertical-align:middle}
.price-box{align-self:flex-end;width:50px;border:1px solid var(--line);text-align:center;padding:5px 0 0;margin-bottom:4px}
.price-box small{display:block;font-size:6px;color:var(--muted)}
.price-box strong{display:block;font-family:"Raleway",sans-serif;font-size:12px;color:var(--brand)}
.price-box .btn{width:100%;height:14px;line-height:14px;margin-top:4px;font-size:6px}
.grounds{text-align:center;margin-top:22px}
.grounds .section-title{font-size:25px}
.cards{display:flex;gap:18px;justify-content:center;margin-top:16px}
.card{width:160px;text-align:center}
.card-photo{height:115px}
.card p{font-size:7px;line-height:1.45;color:var(--muted);margin:8px 8px 6px;height:21px}
.card .btn{width:86px;height:18px;line-height:18px;font-size:7.5px}
.site-footer{position:absolute;left:0;right:0;bottom:0;height:44px;background:var(--footer);display:flex;justify-content:center;align-items:center;font-family:"Raleway",sans-serif;font-size:10px;color:var(--white)}
.site-footer span{padding:0 4px}
</style>
</head>
<body>
<header class="site-header">
  <div class="brand"><span class="brand-dot"></span>Belcourt Manor</div>
  <nav class="main-nav">
    <svg width="12" height="11" viewBox="0 0 12 11"><path d="M6 0L0 5h1.5v6h3.5V7.5h2V11h3.5V5H12z" fill="#1f6fb4"/></svg>
    <span>Home</span><span class="sep">|</span><span>Mansion</span><span class="sep">|</span><span>Bedrooms</span><span class="sep">|</span><span>Options</span><span class="sep">|</span><span>Garden Cottage</span><span class="sep">|</span><span>Grounds</span><span class="sep">|</span><span>Location</span><span class="sep">|</span><span>Gallery</span><span class="sep">|</span><span>Contact</span><span class="sep">|</span><span>Availability</span><span class="sep">|</span><span>Off Weddings</span>
  </nav>
</header>

<section class="hero">
  <div class="hero-photo" role="img" aria-label="Mansion lit at dusk beside palm-lined pool, fading into a soft image of a couple walking"></div>
  <div class="reservation">
    <h2 class="section-title">Resort Reservation</h2>
    <p class="lead">Plan your stay at our private estate resort. Choose your dates and book today.</p>
    <div class="res-form">
      <div class="field"><label>Arrival</label><div></div></div>
      <div class="field"><label>Departure</label><div></div></div>
      <div class="field"><label>Adults</label><div></div></div>
      <div class="field"><label>Children</label><div></div></div>
      <div class="field"><label>Rooms</label><div></div></div>
    </div>
    <span class="btn res-btn">BOOK NOW</span>
  </div>
</section>

<section class="welcome">
  <h2 class="section-title">Welcome to Belcourt Manor</h2>
</section>
<div class="intro">
  <div class="intro-photo" role="img" aria-label="Aerial view of the manor with terracotta roof, pool and gardens"></div>
  <div class="intro-text">
    <div class="intro-copy">
      <h3>Palatial Estate &amp; Luxury Resort</h3>
      <p>Set on five acres of tropical gardens, Belcourt Manor offers a private resort stay with pool, tennis court and spacious living areas for families and groups.</p>
      <p>The mansion features eight bedrooms, a games room, outdoor dining and a resort style lagoon pool, ideal for holidays, reunions and weddings.</p>
      <p>Every stay includes linen, cleaning and friendly local hosts who help plan your visit.</p>
      <ul>
        <li>Sleeps up to twenty guests</li>
        <li>Heated pool and spa</li>
        <li>Walk to local shops</li>
      </ul>
    </div>
    <div class="price-box">
      <small>From</small>
      <strong>$540</strong>
      <small>per night</small>
      <span class="btn">BOOK NOW</span>
    </div>
  </div>
</div>

<section class="grounds">
  <h2 class="section-title">The Grounds</h2>
  <div class="cards">
    <article class="card">
      <div class="card-photo" role="img" aria-label="Lagoon pool with cabana and palms" style="background:linear-gradient(160deg,#8fa86d,#c79a6e 50%,#6bb3d4)"></div>
      <p>Lagoon style pool with private cabana and tropical gardens</p>
      <span class="btn">READ MORE</span>
    </article>
    <article class="card">
      <div class="card-photo" role="img" aria-label="Lit garden pathway under trees" style="background:linear-gradient(160deg,#4f6e3f,#8fb06a 55%,#c8c0a0)"></div>
      <p>Meandering pathways with lighting to all corners of the grounds</p>
      <span class="btn">READ MORE</span>
    </article>
    <article class="card">
      <div class="card-photo" role="img" aria-label="Tennis court surrounded by trees" style="background:linear-gradient(170deg,#7ea3c8,#5d8a4a 45%,#4f8a6a)"></div>
      <p>Full size tennis court with lights and pro shop</p>
      <span class="btn">READ MORE</span>
    </article>
    <article class="card">
      <div class="card-photo" role="img" aria-label="Wooden children's playground on a lawn" style="background:linear-gradient(160deg,#9cbfd9,#7a9a52 55%,#a07a52)"></div>
      <p>Children's playground with adventure fort and swings</p>
      <span class="btn">READ MORE</span>
    </article>
  </div>
</section>

<footer class="site-footer">
  <span>Home</span>|<span>Mansion</span>|<span>Bedrooms</span>|<span>Options</span>|<span>Garden Cottage</span>|<span>Grounds</span>|<span>Location</span>|<span>Gallery</span>|<span>Contact</span>|<span>Availability</span>|<span>Off Weddings</span>
</footer>
</body>
</html>
```